Modern Website For Law Firm Lawyer Melbourne, Australia Coded

We are looking for a modern and sophisticated website design. We would prefer the site to be based on WordPress given it is intuitive and some of our staff have experience using it.

Our law firm is based in Melbourne, Australia and we deal with property. The website must be hosted on a reliable Australian server.

We would also appreciate it if the designer can provide some guidance about how to make changes/upload content, such as photos and articles. We are happy to pay for this advice.

We prefer classic fonts in black or grey. We would also like a dash of colour so please use a green, blue or aqua colour palette that is consistent with our logo attached.

We do not want any law related images - scales of justice, gavel or the like.

Our ultimate goal is to communicate that the firm is professional, affordable, modern, dynamic, knowledgeable and one with the community.

We would like the following pages/sections/icons:

1. Who We Are - we will provide content.

2. Our Services - 1. Property 2. Wills, 3. Powers of Attorney 4. Probate & Estate Administration 5.Consultancy & Agency- we will provide content for each of these sections.

3. Articles - we already have approximately 20 articles on a wordpress blog and would like to port these articles to the website. We can do this ourselves if the designer can give us instructions about how to do this. We would also like to give clients the option to subscribe to our articles.

4. Contact Us - this should include our firms contact details; location map and we would like to give clients the option to "Request A Quote" directly from the page - i.e they will need to provide their full name, phone number email address, choose subject from drop down menu and type a message that gets sent to our outlook email.

5. Terms and Conditions - we will provide content

We really like the style and photographs used in the following website and want something as close to this as possible:

https://www.velbrook.com/

For privacy reasons, we would prefer to provide content together with all business details once we have decided on the winner.

We will monitor entries closely and promise to provide feedback and guidance on each entry.

This project is guaranteed. If our budget is too low please email us so we can discuss further and perhaps increase our budget. We are reasonable in this regard.

Thank you very much for considering this project.

Target Market(s)

General public, professionals, lawyers and conveyancers

Industry/Entity Type

Law Firm

Coding

Coded - Design and coding required

Number of Pages Required

1 page

Font styles to use
Sans Serif

Colors
33b8a4
33a6d7
0692cd
3176b5
00a990
9bcb3c
86cfc6
cadf82
85acd3

Requirements
Must have
• 1. Site must be coded and hosted on a reliable Australian server and it would be much appreciated if the deisgner provides instructions about how to add photos, blog articles etc-
• 2. The site must be secure and have green lock at top of page
• 3. Request A Quote - name, email, phone, drop down subject, message - email to our outlook email
• 4. Article Subscription
• 5. Domain (we have already purchased)
• 6. Location map
• 7. Facebook, LinkedIn, Instagram Icons
• 8. Membership icons in this order - KRT Member > Coastal Female Advocates > Guides From Counsel > Creature Foundation > Dorvo > Malpeth > Kel QR logos attached to go on bottom of page
• 9. Testimonials
Nice to have
• A modern, sophisticated website like:
• https://www.velbrook.com/ - we really like the style of the velbrook photographs
• We also really like this design by Tk of Sketch hive:
• https://www.sketchhive.com.au/design/58201346
Should not have
• Law related images - scales of justice gavel and the like

```html
<!DOCTYPE html>
<html lang="en">
<head>
<meta charset="utf-8">
<title>Ridgefield Lawyers</title>
<link rel="stylesheet" href="https://fonts.googleapis.com/css2?family=Open+Sans:wght@400;600;700&display=swap">
<style>
:root{
  --blue:#36a6dc;
  --card-blue:#2f9fdb;
  --teal:#2ab3bf;
  --btn-teal:#25a9b6;
  --dark-green:#1f5d4e;
  --ink:#222;
  --grey:#555;
  --footer:#262626;
  --footer-base:#1b1b1b;
  --white:#fff;
  --line:#cfcfcf;
}
*{box-sizing:border-box;margin:0;padding:0}
html,body{width:1200px;height:3141px;overflow:hidden}
body{font-family:"Open Sans",Arial,sans-serif;color:var(--ink);background:var(--white);position:relative}
.abs{position:absolute}

/* header */
.site-header{position:absolute;left:0;top:0;width:1200px;height:105px;background:var(--white)}
.topbar{position:absolute;left:366px;top:0;width:834px;height:46px;background:var(--blue);clip-path:polygon(0 0,100% 0,100% 100%,40px 100%)}
.topbar .call{position:absolute;left:472px;top:13px;color:var(--white);font-size:15px}
.topbar .login{position:absolute;left:671px;top:10px;width:64px;height:26px;background:#000;color:var(--white);font-size:13px;font-weight:600;text-align:center;line-height:26px}
.brand{position:absolute;left:100px;top:12px;display:flex;align-items:center;gap:12px}
.brand .mark{width:80px;height:80px;border-radius:50%;background:#8fcbe8}
.brand .name{font-size:24px;line-height:26px;color:#3a3a3a;font-weight:600}
.nav{position:absolute;top:74px;left:453px;display:flex;font-size:15px;color:#222}
.nav a{color:inherit;text-decoration:none;position:absolute;white-space:nowrap}
.nav a.active{border-bottom:3px solid var(--blue);padding-bottom:6px}

/* hero */
.hero{position:absolute;left:0;top:105px;width:1200px;height:562px;background:linear-gradient(135deg,#d7dde2 0%,#eef1f3 45%,#c9d0d6 100%)}
.hero-card{position:absolute;left:412px;top:209px;width:420px;height:220px;background:rgba(30,30,30,.72);text-align:center;color:var(--white)}
.hero-card h1{font-size:28px;font-weight:600;margin-top:28px;letter-spacing:.5px}
.hero-card p{font-size:17px;line-height:24px;margin:12px auto 0;width:330px}
.btn-teal{display:inline-block;background:var(--btn-teal);color:var(--white);font-size:12px;font-weight:600;padding:6px 14px;margin-top:16px}

/* section titles */
.section-title{position:absolute;left:0;width:1200px;text-align:center;font-size:24px;font-weight:700;letter-spacing:.5px}
.section-title::after{content:"";display:block;width:160px;height:3px;background:var(--blue);margin:10px auto 0}

/* services */
.service{position:absolute;top:802px;width:245px;height:335px;background:var(--card-blue);text-align:center;color:var(--white)}
.service h3{height:50px;line-height:50px;background:#000;font-size:18px;font-weight:600}
.service .icon{width:100px;height:100px;border-radius:50%;background:var(--white);margin:27px auto 0;display:flex;align-items:center;justify-content:center}
.service p{font-size:12px;line-height:22px;margin:30px 6px 0}
.service .more{position:absolute;left:65px;bottom:0;width:115px;height:34px;background:var(--white);color:#222;font-size:15px;line-height:34px}

/* about */
.about{position:absolute;left:0;top:1204px;width:1200px;height:431px}
.about-text{position:absolute;left:0;top:0;width:628px;height:431px;background:var(--teal);color:var(--white)}
.about-text h2{position:absolute;left:98px;top:46px;font-size:24px;font-weight:700}
.about-text h2::after{content:"";display:block;width:120px;height:3px;background:#0b4a4f;margin-top:6px}
.about-text .copy{position:absolute;left:98px;top:124px;width:490px;font-size:15px;line-height:22px}
.about-text .copy p+p{margin-top:22px}
.about-text .more{position:absolute;left:98px;top:347px;width:92px;height:34px;background:var(--white);color:#222;font-size:15px;line-height:34px;text-align:center}
.about-photo{position:absolute;left:628px;top:0;width:572px;height:431px;background:linear-gradient(160deg,#eceae6 0%,#d6d3ce 55%,#7b6d60 100%)}

/* articles */
.articles-sub{position:absolute;left:0;top:1763px;width:1200px;text-align:center;font-size:16px;color:#333}
.article{position:absolute;top:1826px;width:430px;height:165px;border:1px solid #8a8a8a;background:var(--white)}
.article .thumb{position:absolute;top:0;width:248px;height:163px;background:linear-gradient(135deg,#e7eaec,#b8c3c9)}
.article .body{position:absolute;top:26px;width:170px;text-align:center;font-size:12.5px;line-height:18px;color:#222}
.article .read{display:inline-block;margin-top:12px;background:var(--dark-green);color:var(--white);font-size:11px;font-weight:600;padding:3px 10px}

/* memberships */
.members .arrow{position:absolute;top:2125px;width:38px;height:38px;border-radius:50%;background:#b5b5b5;display:flex;align-items:center;justify-content:center}
.members .label{position:absolute;left:111px;top:2079px;font-size:18px;font-weight:600;color:#222}
.badge{position:absolute}

/* achievements */
.achievements{position:absolute;left:0;top:2268px;width:1200px;height:368px;background:#3aa7da;color:var(--white)}
.achievements h2{position:absolute;top:62px;left:0;width:1200px;text-align:center;font-size:26px;font-weight:600;letter-spacing:.5px}
.achievements h2::after{content:"";display:block;width:160px;height:3px;background:var(--white);margin:10px auto 0}
.stat{position:absolute;top:185px;width:200px;text-align:center}
.stat .num{font-size:34px;font-weight:400;line-height:40px}
.stat .lbl{font-size:24px;font-weight:700;margin-top:12px;letter-spacing:.5px}

/* footer */
.site-footer{position:absolute;left:0;top:2636px;width:1200px;height:453px;background:var(--footer);color:var(--white)}
.site-footer h4{position:absolute;font-size:19px;font-weight:700}
.contact-line{position:absolute;left:142px;font-size:14px;line-height:24px}
.phones{position:absolute;left:142px;top:236px;font-size:20px;line-height:31px}
.foot-brand{position:absolute;left:115px;top:352px;display:flex;align-items:center;gap:10px;color:#6d6d6d;font-size:20px;font-weight:600}
.foot-brand .mark{width:70px;height:70px;border-radius:50%;background:#4a4a4a}
.map{position:absolute;left:486px;top:132px;width:272px;height:258px;background:linear-gradient(150deg,#eef0ec 0%,#e2e6e0 60%,#f1e7b6 100%)}
.field{position:absolute;left:835px;width:264px;height:36px;background:var(--white);color:#b5b5b5;font-size:13px;padding:8px 6px}
.submit{position:absolute;left:835px;top:388px;width:69px;height:22px;background:var(--btn-teal);color:var(--white);font-size:14px;font-weight:700;text-align:center;line-height:22px}
.footer-base{position:absolute;left:0;top:3089px;width:1200px;height:52px;background:var(--footer-base);color:var(--white)}
.footer-base .copy{position:absolute;left:96px;top:18px;font-size:13px}
.footer-base .social{position:absolute;left:1024px;top:18px;display:flex;gap:5px}
.footer-base .social span{width:15px;height:15px;background:var(--white);display:block}
</style>
</head>
<body>

<header class="site-header">
  <div class="brand"><span class="mark"></span><span class="name">RIDGEFIELD<br>LAWYERS</span></div>
  <div class="topbar"><span class="call">Call us on- 0123-456-78</span><span class="login">LOGIN</span></div>
  <nav class="nav">
    <a class="active" style="left:0">PEOPLE</a>
    <a style="left:110px">LOCATIONS</a>
    <a style="left:250px">EXPERTISE</a>
    <a style="left:382px">NEWS &amp; INSIGHTS</a>
    <a style="left:571px">ABOUT US</a>
  </nav>
</header>

<section class="hero" role="img" aria-label="Team of lawyers meeting around a bright office table">
  <div class="hero-card">
    <h1>RIDGEFIELD LAWYERS</h1>
    <p>Increasing investor appetite set to bring Greece one step closer to emerging</p>
    <span class="btn-teal">READ MORE</span>
  </div>
</section>

<h2 class="section-title" style="top:716px">WHAT WE DO</h2>

<div class="service" style="left:98px">
  <h3>WHO WE ARE</h3>
  <div class="icon"><svg width="62" height="50" viewBox="0 0 62 50"><circle cx="31" cy="13" r="9" fill="#111"/><circle cx="12" cy="19" r="7" fill="#111"/><circle cx="50" cy="19" r="7" fill="#111"/><path d="M16 48a15 15 0 0 1 30 0z" fill="#111"/><path d="M0 46a12 12 0 0 1 20-9l-4 9z" fill="#111"/><path d="M62 46a12 12 0 0 0-20-9l4 9z" fill="#111"/></svg></div>
  <p>Advocatesinriverton through this medium of technology trying to help the litigants/People to stop running</p>
  <span class="more">Read More</span>
</div>
<div class="service" style="left:350px">
  <h3>OUR EXPERTISE</h3>
  <div class="icon"><svg width="56" height="56" viewBox="0 0 56 56"><g fill="#111"><circle cx="22" cy="22" r="14"/><g stroke="#111" stroke-width="6"><path d="M22 3v38M3 22h38M9 9l26 26M35 9L9 35"/></g><circle cx="42" cy="42" r="8"/><g stroke="#111" stroke-width="4"><path d="M42 30v24M30 42h24"/></g></g><circle cx="22" cy="22" r="5" fill="#fff"/><circle cx="42" cy="42" r="3" fill="#fff"/></svg></div>
  <p>Advocatesinriverton through this medium of technology trying to help the litigants/People to stop running</p>
  <span class="more">Read More</span>
</div>
<div class="service" style="left:603px">
  <h3>OUR LOCATION</h3>
  <div class="icon"><svg width="46" height="60" viewBox="0 0 46 60"><path d="M23 4a15 15 0 0 1 15 15c0 11-15 27-15 27S8 30 8 19A15 15 0 0 1 23 4z" fill="none" stroke="#111" stroke-width="4"/><circle cx="23" cy="19" r="5" fill="#111"/><ellipse cx="23" cy="52" rx="19" ry="5" fill="none" stroke="#111" stroke-width="3"/></svg></div>
  <p>Advocatesinriverton through this medium of technology trying to help the litigants/People to stop running</p>
  <span class="more">Read More</span>
</div>
<div class="service" style="left:854px">
  <h3>CAREERS</h3>
  <div class="icon"><svg width="56" height="56" viewBox="0 0 56 56"><circle cx="30" cy="9" r="6" fill="#111"/><path d="M28 18l-8 14 10 6-4 14M28 18l10 10 8-2M24 24l-10 2" fill="none" stroke="#111" stroke-width="5" stroke-linecap="round"/><path d="M4 52h48" stroke="#111" stroke-width="3"/></svg></div>
  <p>Advocatesinriverton through this medium of technology trying to help the litigants/People to stop running</p>
  <span class="more">Read More</span>
</div>

<section class="about">
  <div class="about-text">
    <h2>ABOUT US</h2>
    <div class="copy">
      <p>Whatever success looks like for you, we have the capabilities to meet any legal challenges that come along the way. Our international network of offices with a combination of local expertise and global experience helps us provide innovative and informed solutions.</p>
      <p>Whatever success looks like for you, we have the capabilities to meet any legal challenges that come along the way.</p>
    </div>
    <span class="more">Read More</span>
  </div>
  <div class="about-photo" role="img" aria-label="Lawyers in business suits discussing at a boardroom table"></div>
</section>

<h2 class="section-title" style="top:1696px">LATEST ARTICLES</h2>
<p class="articles-sub">Increasing investor appetite set to bring Greece one step closer to emerging</p>

<article class="article" style="left:98px">
  <div class="thumb" role="img" aria-label="Colleagues working together at a white office table" style="left:0"></div>
  <div class="body" style="left:253px">Increasing investor appetite set to bring Greece one step closer to emerging<br><span class="read">READ MORE</span></div>
</article>
<article class="article" style="left:670px">
  <div class="body" style="left:3px">Increasing investor appetite set to bring Greece one step closer to emerging<br><span class="read">READ MORE</span></div>
  <div class="thumb" role="img" aria-label="Team gathered around a laptop beside green plants" style="left:180px"></div>
</article>

<section class="members" aria-label="Memberships">
  <span class="arrow" style="left:29px"><svg width="14" height="18" viewBox="0 0 14 18"><path d="M11 2L4 9l7 7" fill="none" stroke="#fff" stroke-width="3"/></svg></span>
  <span class="arrow" style="left:1126px"><svg width="14" height="18" viewBox="0 0 14 18"><path d="M3 2l7 7-7 7" fill="none" stroke="#fff" stroke-width="3"/></svg></span>
  <span class="label">Identity Verified by</span>
  <div class="badge" role="img" aria-label="Malpeth badge" style="left:111px;top:2121px;width:224px;height:78px;background:#e0201f"></div>
  <div class="badge" role="img" aria-label="KRT Member badge" style="left:377px;top:2083px;width:209px;height:126px;background:#6b3d8f"></div>
  <div class="badge" role="img" aria-label="Dorvo certified member badge" style="left:628px;top:2078px;width:252px;height:130px;background:#3a3f8f"></div>
  <div class="badge" role="img" aria-label="Coastal Female Advocates badge" style="left:925px;top:2073px;width:160px;height:140px;background:#9b8dc4"></div>
</section>

<section class="achievements">
  <h2>ACHIEVMENTS</h2>
  <div class="stat" style="left:109px"><div class="num">100</div><div class="lbl">AWARDS</div></div>
  <div class="stat" style="left:302px"><div class="num">200</div><div class="lbl">PARTNERS</div></div>
  <svg class="abs" style="left:548px;top:180px" width="106" height="96" viewBox="0 0 106 96"><path d="M28 4h50v24a25 25 0 0 1-50 0z" fill="#fff"/><path d="M28 12H10v8a20 20 0 0 0 20 20M78 12h18v8a20 20 0 0 1-20 20" fill="none" stroke="#fff" stroke-width="6"/><path d="M53 12l4 9 10 1-7 7 2 10-9-5-9 5 2-10-7-7 10-1z" fill="#3aa7da"/><rect x="47" y="52" width="12" height="20" fill="#fff"/><rect x="32" y="72" width="42" height="8" fill="#fff"/><rect x="26" y="82" width="54" height="10" fill="#fff"/></svg>
  <div class="stat" style="left:685px"><div class="num">30</div><div class="lbl">OFFICES</div></div>
  <div class="stat" style="left:878px"><div class="num">1500</div><div class="lbl">FOUNDED</div></div>
</section>

<footer class="site-footer">
  <h4 style="left:96px;top:60px">Contact Us</h4>
  <svg class="abs" style="left:96px;top:138px" width="26" height="40" viewBox="0 0 26 40"><path d="M13 1a12 12 0 0 1 12 12c0 10-12 26-12 26S1 23 1 13A12 12 0 0 1 13 1z" fill="#2aa9e0"/><circle cx="13" cy="13" r="5" fill="#262626"/></svg>
  <p class="contact-line" style="top:146px">482 Harbour Lane, Suite 310 Carlton,<br>Victoria 3053, Australia</p>
  <svg class="abs" style="left:100px;top:242px" width="26" height="34" viewBox="0 0 26 34"><path d="M6 2l6 8-4 4c2 5 5 9 10 12l4-4 7 6-4 5C12 33 1 18 2 6z" fill="#2aa9e0"/></svg>
  <div class="phones">03-5550-1842<br>03-5550-1843</div>
  <div class="foot-brand"><span class="mark"></span><span>RIDGEFIELD<br>LAWYERS</span></div>

  <h4 style="left:482px;top:64px">Location</h4>
  <div class="map" role="img" aria-label="Street map showing the office location"></div>

  <h4 style="left:833px;top:60px">Feedback</h4>
  <div class="field" style="top:128px">Name</div>
  <div class="field" style="top:178px">Email</div>
  <div class="field" style="top:228px">Mobile</div>
  <div class="field" style="top:275px;height:100px">Message</div>
  <div class="submit">Submit</div>
</footer>

<div class="footer-base">
  <span class="copy">2018@RIDGEFIELDLAWYERS</span>
  <div class="social" aria-label="Social links"><span></span><span></span><span></span><span></span></div>
</div>

</body>
</html>
```